New Company Logo & Responsive Website Design for Codeweave Orchard

Codeweave Orchard provides a white labeled, digital lending platform technology solutions to the mortgage industry via a SaaS model. Our target market is Mortgage Companies and Banks who are looking for innovative technology to assist both borrowers and loan originators with the lending process, while automating as much of he process as possible.

Codeweave Orchard is our company name, and our modular software offerings Include the following Products:

1) Applicant Orchard: A customizable, web based, point-of-sale application for borrowers to complete a loan application, and guide them through the mortgage process.

POS Definition
"A point of sale (POS) is the client-facing software solution that allows borrowers to create a customer portal, apply for a loan online, and seamlessly submit needed documentation."

2) Escrowmap Orchard: A Mortgage Loan Origination System

LOS Definition
"A Mortgage Loan Origination System (LOS) is a platform that takes a completed loan application and facilitates the mortgage transaction from origination to post closing. LOS systems may include document management, pricing and eligibility engines, and compliance tools to decrease risk and increase loan manufacturing quality.

3) Dwelling Orchard: A brandable, home search website

The LOS and POS definitions provided above are just for your understanding of what these products are, not to be included word-for-word as website content.

We are looking for designs that are elegant, convey technical competency, simple to navigate, and set us apart from the competition.

We are not set on any particular colors at this point, so feel free to choose the best colors for your particular designs.

Please include company logo, both desktop and mobile designs with a template design for the website sub pages.

Some Examples of Mortgage Technology Websites offering similar products. These are to show the typical content, not designs that we particularly like or dislike.

https://trenvask.com/
https://www.brightquorel.com/
https://www.dwelfundbuddy.com/
https://www.escrowotter.com/
https://www.quennidata.com/products/route

Please send comments with additional questions.

Thank You For your participation.

```html
<!DOCTYPE html>
<html lang="en">
<head>
<meta charset="utf-8">
<title>Codeweave Orchard — Digital Lending Platform</title>
<link rel="stylesheet" href="https://fonts.googleapis.com/css2?family=Montserrat:wght@400;500;600;700&display=swap">
<style>
:root{
  --navy:#0b2a5b;
  --navy-deep:#071f47;
  --blue:#2f6fdc;
  --blue-bright:#3a7bf0;
  --pale:#eef2f9;
  --ink:#1c2430;
  --muted:#555d6b;
  --white:#ffffff;
  --bezel:#17191c;
  --steel:#d3d7dc;
}
*{box-sizing:border-box;margin:0;padding:0}
html,body{width:1200px;height:4494px;overflow:hidden}
body{position:relative;background:var(--white);font-family:"Montserrat",sans-serif;color:var(--ink)}
.backdrop{position:absolute;left:0;top:0;width:1200px;height:4494px}
.abs{position:absolute}
.mock{position:absolute;overflow:visible;font-family:"Montserrat",sans-serif}
.card{filter:drop-shadow(0 6px 14px rgba(11,42,91,.16))}
.brand{display:flex;align-items:center;gap:10px;font-weight:500;letter-spacing:1px;font-size:15px;color:var(--white);text-transform:uppercase;white-space:nowrap}
.nav{top:44px;left:600px;font-size:12.5px;color:var(--white)}
.nav a{position:absolute;color:var(--white);text-decoration:none;white-space:nowrap}
.nav a.active{color:#7fb0ff}
.auth{top:6px;left:920px;display:flex;gap:6px}
.auth span{display:inline-block;height:26px;line-height:26px;padding:0 24px;border-radius:13px;font-size:11px}
.auth .login{background:var(--blue-bright);color:var(--white)}
.auth .register{background:var(--white);color:var(--navy)}
.btn{display:inline-block;height:38px;line-height:38px;padding:0 32px;border-radius:19px;font-size:11px;font-weight:600;letter-spacing:.4px;text-transform:uppercase;text-decoration:none}
.btn-light{background:var(--white);color:var(--navy)}
.btn-blue{background:var(--blue);color:var(--white)}
.eyebrow{font-size:17px;font-weight:400}
.title{font-size:33px;font-weight:500;line-height:1.2}
.copy{font-size:12.5px;line-height:20px;color:var(--muted)}
.center{text-align:center;left:0;width:1200px}
.center .copy{margin:0 auto}
.hero-copy{left:130px;top:178px;width:390px;color:var(--white)}
.hero-copy .eyebrow{font-size:23px}
.hero-copy .title{font-size:42px;margin-top:4px}
.hero-copy .copy{color:#d6e0f3;margin-top:26px}
.hero-copy .btn{margin-top:36px}
.split h3{font-size:22px;font-weight:500;margin-bottom:18px}
.split .copy{margin-bottom:22px}
.mascot{position:absolute;border-radius:46% 46% 40% 40%}
.badge{background:var(--white);box-shadow:0 6px 18px rgba(11,42,91,.12);display:flex;align-items:center;justify-content:center}
.badge .seal{width:70px;height:70px;border-radius:50%}
.footer-col h4{font-size:18px;font-weight:500;color:var(--blue-bright);margin-bottom:14px}
.footer-col li{list-style:none;font-size:12px;color:var(--white);line-height:24px}
.contact{display:flex;align-items:center;gap:10px;font-size:12px;color:var(--white)}
.contact .dot{width:24px;height:24px;border-radius:50%;background:var(--blue);display:flex;align-items:center;justify-content:center}
.social{display:flex;gap:10px}
.social span{width:30px;height:30px;border-radius:50%;border:1.5px solid var(--white)}
.legal{top:4430px;font-size:11px;color:#aab7d0}
.legal b{color:var(--white);font-weight:500}
</style>
</head>
<body>

<svg class="backdrop" viewBox="0 0 1200 4494" aria-hidden="true">
  <path d="M0 0H1120C1215 140 1190 330 1060 460C950 570 700 600 0 618Z" fill="var(--navy)"/>
  <rect x="0" y="956" width="1200" height="520" fill="var(--pale)"/>
  <path d="M0 1490C250 1420 600 1415 1200 1442V1480C650 1455 300 1470 0 1520Z" fill="var(--blue)"/>
  <path d="M0 1472C300 1430 650 1425 1200 1445V1455C640 1440 300 1450 0 1495Z" fill="var(--white)"/>
  <path d="M0 1790C60 1860 170 1930 320 1960C170 1950 60 1900 0 1850Z" fill="var(--blue)"/>
  <path d="M0 2060C350 1990 800 1960 1200 2050V2520H0Z" fill="var(--pale)"/>
  <path d="M600 2005C850 1990 1050 2010 1200 2060V2150C1080 2070 880 2020 600 2005Z" fill="var(--blue)"/>
  <path d="M900 2960C1030 2930 1150 2860 1200 2780V2840C1140 2910 1030 2955 900 2960Z" fill="var(--blue)"/>
  <path d="M0 3000C350 2970 800 2960 1200 2960V3455H0Z" fill="var(--pale)"/>
  <path d="M0 3060C150 3000 320 2980 560 2985C320 2995 150 3030 0 3110Z" fill="var(--blue)"/>
  <polygon points="790,3190 916,3190 790,3330" fill="var(--blue)"/>
  <polygon points="800,3310 922,3300 808,3420" fill="var(--blue)"/>
  <polygon points="290,3548 410,3420 460,3420 350,3548" fill="var(--blue)"/>
  <path d="M0 4100C300 4050 800 4020 1200 4020V4494H0Z" fill="var(--navy)"/>
  <path d="M0 4100C300 4050 800 4020 1200 4020V4060C800 4060 300 4090 0 4140Z" fill="var(--navy-deep)"/>
</svg>

<!-- header -->
<div class="abs brand" style="left:130px;top:16px">Codeweave Orchard</div>
<nav class="abs nav">
  <a class="active" style="left:20px">Home</a>
  <a style="left:92px">About Us</a>
  <a style="left:181px">Products</a>
  <a style="left:268px">Security</a>
  <a style="left:352px">News</a>
  <a style="left:422px">Contacts</a>
</nav>
<div class="abs auth"><span class="login">Login</span><span class="register">Register</span></div>

<!-- hero -->
<section class="abs hero-copy">
  <div class="eyebrow">Your Digital</div>
  <h1 class="title">Lending Platform</h1>
  <p class="copy">Sed ut perspiciatis unde omnis iste natus error sit voluptatem accusantium doloremque laudantium, totam rem aperiam, eaque ipsa quae ab illo inventore veritatis et quasi architecto beatae vitae dicta sunt explicabo.</p>
  <a class="btn btn-light">Learn More</a>
</section>

<svg class="mock" style="left:480px;top:130px;width:630px;height:460px" viewBox="480 130 630 460" role="img" aria-label="Lending dashboard on a desktop monitor, with a tablet and a summary card">
  <polygon points="748,485 858,485 872,560 734,560" fill="#c9ced4"/>
  <ellipse cx="803" cy="566" rx="84" ry="9" fill="#b9bfc6"/>
  <rect x="532" y="153" width="541" height="332" rx="8" fill="var(--bezel)"/>
  <rect x="542" y="163" width="521" height="312" fill="#fff"/>
  <rect x="542" y="163" width="521" height="12" fill="#26313f"/>
  <rect x="990" y="166" width="24" height="6" fill="#3bb56b"/>
  <rect x="542" y="175" width="100" height="300" fill="#2e3a4a"/>
  <text x="558" y="222" font-size="11" font-weight="700" fill="#fff">4.65</text>
  <text x="598" y="222" font-size="11" font-weight="700" fill="#fff">1161</text>
  <g fill="#56657a">
    <rect x="552" y="240" width="80" height="3"/><rect x="552" y="290" width="70" height="3"/>
    <rect x="552" y="300" width="78" height="3"/><rect x="552" y="310" width="64" height="3"/>
    <rect x="552" y="320" width="76" height="3"/><rect x="552" y="350" width="70" height="3"/>
    <rect x="552" y="360" width="60" height="3"/><rect x="552" y="370" width="74" height="3"/>
    <rect x="552" y="380" width="68" height="3"/><rect x="552" y="390" width="72" height="3"/>
  </g>
  <rect x="798" y="196" width="66" height="34" fill="#fff" stroke="#c5ccd6"/>
  <rect x="800" y="214" width="62" height="5" fill="#3a7bf0"/>
  <line x1="690" y1="228" x2="1040" y2="228" stroke="#cfd5dd"/>
  <rect x="690" y="222" width="24" height="6" fill="#2e3a4a"/>
  <rect x="960" y="222" width="10" height="6" fill="#2e3a4a"/>
  <rect x="690" y="283" width="60" height="5" fill="#e3e7ec"/>
  <rect x="770" y="283" width="34" height="5" fill="#e3e7ec"/>
  <line x1="695" y1="325" x2="695" y2="428" stroke="#cfd5dd"/>
  <line x1="695" y1="428" x2="985" y2="428" stroke="#cfd5dd"/>
  <g fill="#5e7e9f">
    <rect x="700" y="345" width="8" height="83"/><rect x="712" y="358" width="8" height="70"/>
    <rect x="724" y="380" width="8" height="48"/><rect x="736" y="392" width="8" height="36"/>
    <rect x="748" y="398" width="8" height="30"/><rect x="760" y="402" width="8" height="26"/>
    <rect x="772" y="405" width="8" height="23"/><rect x="784" y="408" width="8" height="20"/>
    <rect x="796" y="410" width="8" height="18"/><rect x="808" y="411" width="8" height="17"/>
    <rect x="820" y="412" width="8" height="16"/><rect x="832" y="413" width="8" height="15"/>
    <rect x="844" y="414" width="8" height="14"/><rect x="856" y="415" width="8" height="13"/>
    <rect x="868" y="416" width="8" height="12"/><rect x="880" y="418" width="8" height="10"/>
    <rect x="892" y="419" width="8" height="9"/><rect x="904" y="420" width="8" height="8"/>
    <rect x="916" y="421" width="8" height="7"/><rect x="928" y="422" width="8" height="6"/>
  </g>
  <rect x="1018" y="280" width="45" height="195" fill="#2e3a4a"/>
  <rect x="1040" y="335" width="8" height="30" fill="#f2c12e"/>
  <g class="card">
    <rect x="1024" y="136" width="70" height="99" rx="4" fill="#fff"/>
  </g>
  <rect x="1030" y="142" width="58" height="4" fill="#c7cdd6"/>
  <text x="1040" y="165" font-size="8" fill="#8a93a0">$12,456</text>
  <rect x="1030" y="178" width="58" height="14" fill="#eef1f5"/>
  <circle cx="1060" cy="212" r="5" fill="#e0453a"/>
  <rect x="1030" y="224" width="58" height="3" fill="#c7cdd6"/>
  <g class="card">
    <rect x="488" y="394" width="156" height="112" rx="6" fill="#fff" stroke="#d5dae1"/>
  </g>
  <rect x="498" y="402" width="8" height="96" fill="#2e3a4a"/>
  <rect x="512" y="402" width="124" height="10" fill="#e5e9ef"/>
  <rect x="512" y="416" width="30" height="8" fill="#e0453a"/>
  <rect x="546" y="416" width="30" height="8" fill="#c14e8e"/>
  <rect x="580" y="416" width="30" height="8" fill="#5a6cc0"/>
  <rect x="614" y="416" width="22" height="8" fill="#2fa3b4"/>
  <polyline points="512,450 528,440 544,452 560,436 576,448 592,438 608,450 624,440" fill="none" stroke="#e0453a" stroke-width="1.4"/>
  <circle cx="572" cy="482" r="11" fill="none" stroke="#5a6cc0" stroke-width="4"/>
  <rect x="600" y="468" width="32" height="28" rx="3" fill="#c14e8e"/>
  <rect x="512" y="470" width="40" height="26" fill="#f3f5f8"/>
</svg>

<!-- welcome -->
<section class="abs center" style="top:668px">
  <div class="eyebrow">Welcome To</div>
  <h2 class="title" style="margin-top:6px">Codeweave Orchard</h2>
  <p class="copy" style="width:900px;margin-top:22px">Sed ut perspiciatis unde omnis iste natus error sit voluptatem accusantium doloremque laudantium, totam rem aperiam, eaque ipsa quae ab illo inventore veritatis et quasi architecto beatae vitae dicta sunt explicabo. Nemo enim ipsam voluptatem quia voluptas sit aspernatur aut odit aut fugit, sed quia consequuntur magni dolores eos qui ratione voluptatem sequi nesciunt.</p>
  <a class="btn btn-blue" style="margin-top:26px">Learn More</a>
</section>

<!-- automated -->
<section class="abs center" style="top:1006px">
  <div class="eyebrow">Enjoy The Benefit od a</div>
  <h2 class="title" style="margin-top:6px">Fully Automated Mortgage Operation</h2>
  <p class="copy" style="width:820px;margin-top:18px">Sed ut perspiciatis unde omnis iste natus error sit voluptatem accusantium doloremque laudantium, totam rem aperiam, eaque ipsa quae ab illo inventore veritatis et quasi architecto beatae vitae dicta sunt explicabo.</p>
</section>
<svg class="mock" style="left:330px;top:1110px;width:540px;height:350px" viewBox="330 1110 540 350" aria-hidden="true">
  <defs>
    <linearGradient id="housePhoto" x1="0" y1="0" x2="0" y2="1">
      <stop offset="0" stop-color="#c8cfd6"/><stop offset=".45" stop-color="#b49c7e"/><stop offset="1" stop-color="#8b969f"/>
    </linearGradient>
    <radialGradient id="glow" cx=".5" cy=".5" r=".5">
      <stop offset="0" stop-color="#dbe6f7"/><stop offset="1" stop-color="#dbe6f7" stop-opacity="0"/>
    </radialGradient>
  </defs>
  <circle cx="600" cy="1250" r="150" fill="url(#glow)"/>
  <rect x="395" y="1160" width="410" height="272" rx="12" fill="var(--bezel)"/>
  <path d="M345 1432H855V1438C855 1446 840 1450 820 1450H380C360 1450 345 1446 345 1438Z" fill="#cfd3d8"/>
  <rect x="560" y="1432" width="80" height="5" rx="2" fill="#aeb4bb"/>
</svg>
<div class="abs" role="img" aria-label="Photo of a hand holding a small model house in front of a street of homes" style="left:403px;top:1174px;width:394px;height:247px;background:linear-gradient(180deg,#c8cfd6,#b49c7e 45%,#8b969f)"></div>

<!-- applicant orchard -->
<section class="abs center" style="top:1512px">
  <h2 class="title">Applicant Orchard</h2>
  <p class="copy" style="width:700px;margin-top:14px">A customizable, web based, point-of-sale application for borrowers to complete a loan application, and guide them through the mortgage process.</p>
</section>
<section class="abs split" style="left:130px;top:1710px;width:480px">
  <h3>POS Definition</h3>
  <p class="copy">A point of sale (POS) is the client-facing software solution that allows borrowers to create a customer portal, apply for a loan online, and seamlessly submit needed documentation.</p>
  <a class="btn btn-blue">Learn More</a>
</section>
<svg class="mock" style="left:630px;top:1630px;width:450px;height:330px" viewBox="630 1630 450 330" role="img" aria-label="Borrower portal dashboard with loan totals, a trend chart and score gauges">
  <g class="card"><rect x="642" y="1640" width="427" height="310" fill="#fff"/></g>
  <circle cx="664" cy="1655" r="6" fill="#c4ccd8"/>
  <rect x="642" y="1672" width="103" height="278" fill="#2b5aa8"/>
  <rect x="642" y="1676" width="103" height="14" fill="#244e93"/>
  <text x="656" y="1686" font-size="6" font-weight="600" fill="#fff">Dashboard</text>
  <g fill="#8eb0e2"><rect x="656" y="1700" width="40" height="3"/><rect x="656" y="1720" width="44" height="3"/><rect x="656" y="1740" width="36" height="3"/><rect x="656" y="1760" width="48" height="3"/><rect x="656" y="1780" width="34" height="3"/></g>
  <rect x="745" y="1672" width="324" height="20" fill="#f3f5f9"/>
  <text x="757" y="1686" font-size="6.5" font-weight="700" fill="#2b3a55">DASHBOARD</text>
  <g fill="#c3cad5"><rect x="825" y="1681" width="28" height="3"/><rect x="880" y="1681" width="20" height="3"/><rect x="916" y="1681" width="40" height="3"/></g>
  <rect x="855" y="1700" width="214" height="14" fill="#5b8fd6"/>
  <g fill="#cfd6e0"><rect x="757" y="1705" width="40" height="3"/><rect x="757" y="1716" width="60" height="8"/><rect x="757" y="1740" width="40" height="3"/><rect x="757" y="1750" width="60" height="8"/><rect x="757" y="1775" width="40" height="3"/><rect x="757" y="1785" width="60" height="8"/></g>
  <rect x="757" y="1810" width="60" height="9" rx="4" fill="#e0453a"/>
  <text x="862" y="1736" font-size="10" font-weight="700" fill="#e0453a">$22.5M</text>
  <text x="960" y="1736" font-size="10" font-weight="700" fill="#e0453a">$52.3M</text>
  <g fill="#9aa3b1"><rect x="845" y="1760" width="22" height="3"/><rect x="890" y="1760" width="22" height="3"/><rect x="938" y="1760" width="22" height="3"/><rect x="985" y="1760" width="22" height="3"/><rect x="1030" y="1760" width="22" height="3"/></g>
  <line x1="868" y1="1820" x2="868" y2="1870" stroke="#d5dae1"/>
  <polyline points="872,1860 885,1850 898,1858 911,1842 924,1856 937,1846 950,1852 963,1838 976,1850 989,1840 1002,1848 1015,1832 1028,1846 1041,1836 1060,1826" fill="none" stroke="#3a7bf0" stroke-width="1.3"/>
  <polyline points="872,1866 890,1858 908,1864 926,1852 944,1860 962,1848 980,1858 998,1846 1016,1856 1034,1844 1060,1850" fill="none" stroke="#e0453a" stroke-width="1"/>
  <circle cx="878" cy="1920" r="18" fill="none" stroke="#9db4d8" stroke-width="3" stroke-dasharray="3 3"/>
  <text x="878" y="1925" font-size="14" text-anchor="middle" fill="#3b4658">80</text>
  <circle cx="975" cy="1920" r="18" fill="none" stroke="#f08a3c" stroke-width="3" stroke-dasharray="3 3"/>
  <text x="975" y="1925" font-size="14" text-anchor="middle" fill="#3b4658">98</text>
  <path d="M1050 1935A16 16 0 0 1 1064 1908" fill="none" stroke="#9db4d8" stroke-width="3" stroke-dasharray="3 3"/>
</svg>
<div class="mascot" role="img" aria-label="Small blue robot mascot waving" style="left:600px;top:1826px;width:82px;height:96px;background:radial-gradient(circle at 50% 40%,#6e9fe0,#2f5fa8)"></div>

<!-- escrowmap orchard -->
<section class="abs center" style="top:2052px">
  <h2 class="title">Escrowmap Orchard</h2>
  <p class="copy" style="margin-top:12px">A Mortgage Loan Origination System</p>
</section>
<svg class="mock" style="left:120px;top:2140px;width:500px;height:330px" viewBox="120 2140 500 330" role="img" aria-label="Loan origination dashboard with line, donut and bar charts and progress lists">
  <g class="card"><rect x="131" y="2149" width="471" height="310" fill="#fff"/></g>
  <rect x="131" y="2149" width="85" height="310" fill="#1f2a2e"/>
  <rect x="141" y="2160" width="18" height="16" fill="none" stroke="#3bb56b" stroke-width="1.5"/>
  <rect x="164" y="2165" width="36" height="3" fill="#8d979b"/>
  <rect x="131" y="2205" width="85" height="14" fill="#27353a"/>
  <g fill="#3bb56b"><rect x="143" y="2209" width="6" height="6"/><circle cx="192" cy="2232" r="3"/><circle cx="192" cy="2292" r="3"/></g>
  <g fill="#7a8589"><rect x="156" y="2211" width="30" height="3"/><rect x="156" y="2231" width="24" height="3"/><rect x="156" y="2251" width="20" height="3"/><rect x="156" y="2271" width="26" height="3"/><rect x="156" y="2291" width="22" height="3"/><rect x="156" y="2311" width="26" height="3"/><rect x="156" y="2340" width="24" height="3"/></g>
  <rect x="216" y="2149" width="386" height="18" fill="#f5f6f8"/>
  <rect x="300" y="2154" width="160" height="9" rx="2" fill="#fff" stroke="#e2e5ea"/>
  <rect x="225" y="2175" width="235" height="62" fill="#fff" stroke="#eef0f3"/>
  <polyline points="235,2222 255,2212 275,2208 295,2200 315,2214 335,2206 355,2218 375,2204 395,2196 415,2194 435,2188 450,2182" fill="none" stroke="#e0453a" stroke-width="1.5"/>
  <polyline points="235,2215 260,2210 285,2205 310,2212 335,2200 360,2204 385,2198 410,2200 450,2196" fill="none" stroke="#f2a33a" stroke-width="1"/>
  <rect x="290" y="2196" width="14" height="6" fill="#f2a33a"/><rect x="342" y="2210" width="14" height="6" fill="#e0453a"/><rect x="398" y="2184" width="14" height="6" fill="#2fa3b4"/>
  <rect x="225" y="2245" width="70" height="75" fill="#fff" stroke="#eef0f3"/>
  <circle cx="260" cy="2280" r="16" fill="none" stroke="#e5e8ec" stroke-width="6"/>
  <circle cx="260" cy="2280" r="16" fill="none" stroke="#3bb56b" stroke-width="6" stroke-dasharray="65 100" transform="rotate(-90 260 2280)"/>
  <text x="260" y="2283" font-size="8" text-anchor="middle" fill="#3b4658">65%</text>
  <rect x="240" y="2307" width="40" height="6" fill="#3bb56b"/>
  <rect x="303" y="2245" width="70" height="75" fill="#fff" stroke="#eef0f3"/>
  <polyline points="312,2300 325,2290 338,2294 350,2278 365,2270" fill="none" stroke="#8c9a3a" stroke-width="1.4"/>
  <rect x="318" y="2307" width="40" height="6" fill="#2fa3b4"/>
  <rect x="381" y="2245" width="70" height="75" fill="#fff" stroke="#eef0f3"/>
  <g fill="#f2a33a"><rect x="392" y="2290" width="8" height="20"/><rect x="404" y="2280" width="8" height="30"/></g>
  <g fill="#e0453a"><rect x="416" y="2272" width="8" height="38"/><rect x="428" y="2286" width="8" height="24"/></g>
  <rect x="225" y="2330" width="100" height="120" fill="#fff" stroke="#eef0f3"/>
  <g><rect x="235" y="2350" width="80" height="3" fill="#e0453a"/><rect x="235" y="2362" width="70" height="3" fill="#f2a33a"/><rect x="235" y="2374" width="84" height="3" fill="#3bb56b"/><rect x="235" y="2386" width="60" height="3" fill="#2fa3b4"/><rect x="235" y="2398" width="76" height="3" fill="#e0453a"/><rect x="235" y="2410" width="66" height="3" fill="#f2a33a"/></g>
  <rect x="345" y="2330" width="105" height="120" fill="#fff" stroke="#eef0f3"/>
  <g fill="#cfd5dd"><rect x="355" y="2350" width="30" height="3"/><rect x="355" y="2362" width="30" height="3"/><rect x="355" y="2374" width="30" height="3"/><rect x="355" y="2386" width="30" height="3"/></g>
  <g><rect x="410" y="2350" width="30" height="5" fill="#e0453a"/><rect x="410" y="2362" width="24" height="5" fill="#3bb56b"/><rect x="410" y="2374" width="28" height="5" fill="#2fa3b4"/><rect x="410" y="2386" width="20" height="5" fill="#f2a33a"/></g>
  <rect x="470" y="2175" width="125" height="275" fill="#fff" stroke="#eef0f3"/>
  <g fill="#d8dde3"><rect x="480" y="2195" width="70" height="3"/><rect x="480" y="2205" width="60" height="3"/><rect x="480" y="2215" width="66" height="3"/><rect x="480" y="2225" width="50" height="3"/></g>
  <g fill="#1f2a2e"><rect x="490" y="2275" width="5" height="40"/><rect x="510" y="2285" width="5" height="30"/><rect x="530" y="2265" width="5" height="50"/><rect x="550" y="2280" width="5" height="35"/></g>
  <g fill="#3bb56b"><rect x="497" y="2290" width="5" height="25"/><rect x="517" y="2270" width="5" height="45"/><rect x="537" y="2292" width="5" height="23"/><rect x="557" y="2268" width="5" height="47"/></g>
  <circle cx="505" cy="2400" r="14" fill="none" stroke="#5a6470" stroke-width="5" stroke-dasharray="50 100"/>
</svg>
<div class="mascot" role="img" aria-label="Small beige robot mascot waving" style="left:525px;top:2368px;width:76px;height:94px;background:radial-gradient(circle at 50% 40%,#e8d9c2,#b59a78)"></div>
<section class="abs split" style="left:596px;top:2196px;width:480px">
  <h3>LOS Definition</h3>
  <p class="copy">A Mortgage Loan Origination System (LOS) is a platform that takes a completed loan application and facilitates the mortgage transaction from origination to post closing. LOS systems may include document management, pricing and eligibility engines, and compliance tools to decrease risk and increase loan manufacturing quality.</p>
  <a class="btn btn-blue">Learn More</a>
</section>

<!-- dwelling orchard -->
<section class="abs split" style="left:130px;top:2632px;width:430px">
  <h3 style="font-size:33px;font-weight:500;margin-bottom:24px">Dwelling Orchard</h3>
  <p class="copy">Sed ut perspiciatis unde omnis iste natus error sit voluptatem accusantium doloremque laudantium, totam rem aperiam, eaque ipsa quae ab illo inventore veritatis et quasi architecto beatae vitae dicta sunt explicabo. Nemo enim ipsam voluptatem quia voluptas sit aspernatur aut odit aut fugit, sed quia consequuntur magni dolores eos qui ratione voluptatem sequi nesciunt.</p>
  <a class="btn btn-blue">Learn More</a>
</section>
<svg class="mock" style="left:570px;top:2580px;width:530px;height:350px" viewBox="570 2580 530 350" role="img" aria-label="Home search dashboard on a laptop and a phone, with stat tiles, pie charts and a trend line">
  <defs><linearGradient id="phoneHead" x1="0" x2="1"><stop offset="0" stop-color="#f06a8a"/><stop offset="1" stop-color="#f5a14a"/></linearGradient></defs>
  <rect x="637" y="2593" width="392" height="262" rx="9" fill="var(--bezel)"/>
  <rect x="645" y="2601" width="376" height="246" fill="#fff"/>
  <rect x="645" y="2601" width="50" height="246" fill="#f1f3f7"/>
  <g fill="#c9d0da"><rect x="652" y="2625" width="34" height="3"/><rect x="652" y="2637" width="28" height="3"/><rect x="652" y="2649" width="32" height="3"/></g>
  <text x="713" y="2617" font-size="7" font-weight="600" fill="#2b5aa8">Dashboard</text>
  <rect x="705" y="2632" width="58" height="30" fill="#3d6fb6"/>
  <rect x="767" y="2632" width="58" height="30" fill="#8e5ba8"/>
  <rect x="829" y="2632" width="58" height="30" fill="#c58ab4"/>
  <rect x="891" y="2632" width="58" height="30" fill="#d9534f"/>
  <rect x="953" y="2632" width="58" height="30" fill="#4a7fb5"/>
  <g fill="#fff"><rect x="712" y="2650" width="26" height="4"/><rect x="774" y="2650" width="26" height="4"/><rect x="836" y="2650" width="20" height="4"/><rect x="898" y="2650" width="26" height="4"/><rect x="960" y="2650" width="20" height="4"/></g>
  <circle cx="738" cy="2700" r="14" fill="#3a7bf0"/><path d="M738 2700V2686A14 14 0 0 1 752 2700Z" fill="#f5a14a"/>
  <g fill="#d5dbe3"><rect x="765" y="2690" width="40" height="3"/><rect x="765" y="2700" width="34" height="3"/><rect x="765" y="2710" width="38" height="3"/></g>
  <circle cx="865" cy="2700" r="14" fill="#3a7bf0"/><path d="M865 2700V2686A14 14 0 0 1 877 2707Z" fill="#f5a14a"/>
  <g fill="#d5dbe3"><rect x="900" y="2690" width="40" height="3"/><rect x="900" y="2700" width="34" height="3"/><rect x="900" y="2710" width="38" height="3"/></g>
  <polyline points="745,2780 770,2776 795,2786 820,2790 845,2788 870,2800 895,2812 920,2806 945,2820 975,2830" fill="none" stroke="#3bb56b" stroke-width="1.4"/>
  <path d="M620 2855H1072V2860C1072 2865 1060 2867 1048 2867H644C632 2867 620 2865 620 2860Z" fill="#cfd3d8"/>
  <rect x="591" y="2656" width="129" height="262" rx="16" fill="#222"/>
  <rect x="598" y="2670" width="115" height="236" rx="6" fill="#fff"/>
  <rect x="604" y="2690" width="103" height="26" rx="3" fill="url(#phoneHead)"/>
  <circle cx="655" cy="2770" r="26" fill="none" stroke="#7b5cc9" stroke-width="7"/>
  <path d="M655 2744A26 26 0 0 1 681 2770" fill="none" stroke="#f5a14a" stroke-width="7"/>
  <g fill="#d5dbe3"><rect x="608" y="2815" width="90" height="3"/><rect x="608" y="2827" width="80" height="3"/><rect x="608" y="2839" width="86" height="3"/><rect x="608" y="2851" width="70" height="3"/></g>
  <rect x="606" y="2868" width="36" height="10" rx="2" fill="#3a7bf0"/>
</svg>
<div class="mascot" role="img" aria-label="Small orange robot mascot waving" style="left:985px;top:2672px;width:90px;height:100px;background:radial-gradient(circle at 50% 40%,#f59a6a,#d8542e)"></div>

<!-- security -->
<section class="abs center" style="top:3046px">
  <h2 class="title">Codeweave Orchard Security</h2>
  <p class="copy" style="width:930px;margin-top:18px">Sed ut perspiciatis unde omnis iste natus error sit voluptatem accusantium doloremque laudantium, totam rem aperiam, eaque ipsa quae ab illo inventore veritatis et quasi architecto beatae vitae dicta sunt explicabo. Nemo enim ipsam voluptatem quia voluptas sit aspernatur aut odit aut fugit, sed quia consequuntur magni dolores eos qui ratione voluptatem sequi nesciunt.</p>
</section>
<svg class="mock" style="left:360px;top:3185px;width:480px;height:365px" viewBox="360 3185 480 365" role="img" aria-label="Security protection status dashboard on a monitor with a gauge and alert list">
  <polygon points="572,3479 648,3479 660,3538 560,3538" fill="#c9ced4"/>
  <ellipse cx="610" cy="3542" rx="62" ry="7" fill="#b9bfc6"/>
  <rect x="366" y="3193" width="466" height="286" rx="8" fill="var(--bezel)"/>
  <rect x="376" y="3203" width="446" height="266" fill="#fff"/>
  <rect x="376" y="3203" width="446" height="14" fill="#2a2f36"/>
  <rect x="472" y="3203" width="30" height="14" fill="#2f6fdc"/>
  <g fill="#8e97a3"><rect x="386" y="3208" width="60" height="3"/><rect x="510" y="3208" width="26" height="3"/><rect x="546" y="3208" width="24" height="3"/><rect x="578" y="3208" width="18" height="3"/></g>
  <rect x="376" y="3217" width="124" height="252" fill="#f3f4f6"/>
  <rect x="376" y="3238" width="124" height="12" fill="#2f6fdc"/>
  <g fill="#9aa2ad"><rect x="396" y="3260" width="36" height="3"/><rect x="386" y="3290" width="40" height="3"/><rect x="396" y="3308" width="30" height="3"/><rect x="396" y="3324" width="28" height="3"/><rect x="396" y="3340" width="50" height="3"/><rect x="396" y="3356" width="54" height="3"/><rect x="396" y="3380" width="44" height="3"/></g>
  <g fill="none" stroke="#8e97a3"><circle cx="388" cy="3309" r="4"/><circle cx="388" cy="3325" r="4"/><circle cx="388" cy="3341" r="4"/><circle cx="388" cy="3357" r="4"/><circle cx="388" cy="3381" r="4"/></g>
  <g fill="#9aa2ad"><rect x="510" y="3224" width="30" height="3"/><rect x="510" y="3250" width="60" height="3"/><rect x="752" y="3250" width="56" height="3"/><rect x="752" y="3322" width="56" height="3"/><rect x="752" y="3388" width="56" height="3"/></g>
  <line x1="746" y1="3246" x2="746" y2="3445" stroke="#e3e6ea"/>
  <path d="M557 3338A68 68 0 0 1 693 3338" fill="none" stroke="#e8eaed" stroke-width="12"/>
  <path d="M557 3338A68 68 0 0 1 660 3279" fill="none" stroke="#b9d23a" stroke-width="12"/>
  <path d="M660 3279A68 68 0 0 1 690 3315" fill="none" stroke="#e0453a" stroke-width="12"/>
  <text x="625" y="3330" font-size="20" text-anchor="middle" fill="#3b4658">67</text>
  <text x="625" y="3345" font-size="8" text-anchor="middle" fill="#8e97a3">Computers</text>
  <circle cx="778" cy="3290" r="12" fill="none" stroke="#e3e6ea" stroke-width="3"/>
  <g><rect x="760" y="3336" width="4" height="4" fill="#e0453a"/><rect x="760" y="3346" width="4" height="4" fill="#e0453a"/><rect x="760" y="3356" width="4" height="4" fill="#e0453a"/></g>
  <g fill="#c7cdd6"><rect x="548" y="3368" width="46" height="3"/><rect x="604" y="3368" width="40" height="3"/><rect x="654" y="3368" width="40" height="3"/><rect x="548" y="3378" width="50" height="3"/></g>
  <polygon points="520,3400 526,3390 532,3400" fill="#e0453a"/>
  <rect x="540" y="3394" width="150" height="3" fill="#e0453a"/>
  <rect x="540" y="3402" width="50" height="3" fill="#e0453a"/>
</svg>
<div class="mascot" role="img" aria-label="Orange robot mascot waving beside the monitor" style="left:252px;top:3282px;width:116px;height:150px;background:radial-gradient(circle at 50% 40%,#f59a6a,#d8542e)"></div>

<!-- partners + productivity -->
<div class="abs badge" role="img" aria-label="Partner badge" style="left:130px;top:3624px;width:220px;height:152px"><span class="seal" style="background:linear-gradient(135deg,#f5a14a,#7b3fc4)"></span></div>
<div class="abs badge" role="img" aria-label="Partner badge" style="left:370px;top:3648px;width:220px;height:152px"><span class="seal" style="background:linear-gradient(135deg,#e85aa8,#5a6cf0)"></span></div>
<div class="abs badge" role="img" aria-label="Partner badge" style="left:130px;top:3798px;width:220px;height:152px"><span class="seal" style="background:linear-gradient(135deg,#f0903a,#c44ab8)"></span></div>
<div class="abs badge" role="img" aria-label="Partner badge" style="left:370px;top:3824px;width:220px;height:152px"><span class="seal" style="background:linear-gradient(135deg,#f5a14a,#6b3fd0)"></span></div>
<section class="abs split" style="left:633px;top:3640px;width:440px">
  <div class="eyebrow">Harness The Efficiency of</div>
  <h2 class="title" style="font-size:35px;margin:6px 0 28px">Integrated Productivity Solution</h2>
  <p class="copy">Sed ut perspiciatis unde omnis iste natus error sit voluptatem accusantium doloremque laudantium, totam rem aperiam, eaque ipsa quae ab illo inventore veritatis et quasi architecto beatae vitae dicta sunt explicabo. Nemo enim ipsam voluptatem quia voluptas sit aspernatur aut odit aut fugit, sed quia consequuntur magni dolores eos qui ratione voluptatem sequi nesciunt.</p>
  <a class="btn btn-blue" style="margin-top:8px">Learn More</a>
</section>

<!-- footer -->
<footer>
  <div class="abs brand" style="left:398px;top:4160px">Codeweave Orchard</div>
  <div class="abs contact" style="left:398px;top:4226px"><span class="dot"><svg width="12" height="12" viewBox="0 0 24 24"><path fill="#fff" d="M6.6 10.8a15 15 0 0 0 6.6 6.6l2.2-2.2a1 1 0 0 1 1-.25 11.4 11.4 0 0 0 3.6.57 1 1 0 0 1 1 1V20a1 1 0 0 1-1 1A17 17 0 0 1 3 4a1 1 0 0 1 1-1h3.5a1 1 0 0 1 1 1c0 1.25.2 2.45.57 3.57a1 1 0 0 1-.25 1Z"/></svg></span>+2 (555) 240 7316</div>
  <div class="abs contact" style="left:398px;top:4265px"><span class="dot"><svg width="12" height="12" viewBox="0 0 24 24"><path fill="#fff" d="M3 5h18v14H3Zm2 2v.5l7 4.5 7-4.5V7Z"/></svg></span>hello@codeweaveorchard.com</div>
  <div class="abs social" style="left:396px;top:4338px"><span></span><span></span><span></span></div>
  <div class="abs footer-col" style="left:633px;top:4150px"><h4>Quick Links</h4><ul><li>Home</li><li>About Us</li><li>Products</li><li>Security</li><li>News</li><li>Contacts</li></ul></div>
  <div class="abs footer-col" style="left:809px;top:4150px"><h4>Products</h4><ul><li>Applicant Orchard</li><li>Escrowmap Orchard</li><li>Dwelling Orchard</li></ul></div>
  <div class="abs footer-col" style="left:980px;top:4150px"><h4>Features</h4><ul><li>FinTech POS</li><li>FinTech LOS</li><li>Communication</li><li>Integration</li><li>Mobile Apps</li></ul></div>
  <p class="abs center legal">Copyright © 2022 <b>Codeweave Orchard</b>. All Rights Reserved.</p>
</footer>

</body>
</html>
```